VORIK FLYER 2019

Hi, We need an A4 flyer design for our cleaning company, focusing on dry carpet cleaning I attached our catalogue to give some idea. In addition, our websites can provide more information. Our Services:-General Cleaning Carry out heavy cleansing tasks and special projects. Clean, stock and supply designated facility areas (dusting, sweeping, vacuuming, mopping, cleaning ceiling vents, restroom cleaning etc).Using electrically powered scrubbing and polishing machines to burnish, scrub, polish and spray clean floors. Window Cleaning Regular, Reliable Window Cleaning. Hard To Reach Windows. Single 7 Multi-Storey. Frames and Glass Cleaned. Floor Cleaning Marble Cleaning & Polishing. Tile & Grout Cleaning. Hardwood Floors Services. Vinyl Floors. The BRAM Dry Extraction Carpet Cleaning System uses environmentally preferred, Blue Crest Certified cleaning products that deep cleans your carpets and textured hard floors quickly and easily.

Target Market(s)

Residential and Commercial.
Offices, Hospitals, Restaurants, Etc.

Industry/Entity Type

Cleaning Service

Font styles to use
Serif
Sans Serif

Colors
33a6d7
0592cd
85cae6
85acd3
3277b5
296eb1

Requirements
Must have
• CREATIVE AND MINIMAL
Nice to have
• Engaging Pics and Texts

```html
<!DOCTYPE html>
<html lang="en">
<head>
<meta charset="utf-8">
<title>Vorik Cleaning &amp; Maintenance Flyer</title>
<link rel="stylesheet" href="https://fonts.googleapis.com/css2?family=Montserrat:ital,wght@0,400;0,600;0,700;1,400&family=Open+Sans:wght@400;600&display=swap">
<style>
:root{
  --backdrop:#2c2276;
  --navy:#2a2274;
  --navy-deep:#221c63;
  --paper:#ffffff;
  --panel-light:rgba(238,240,244,.88);
  --ink:#1c1c2a;
  --footer:#2a2a2e;
  --footer-text:#e6e6ea;
  --icon-ring:#2a2274;
}
*{margin:0;padding:0;box-sizing:border-box}
html,body{width:1179px;height:1200px;overflow:hidden;background:var(--backdrop)}
.canvas{position:relative;width:1179px;height:1200px}
.flyer{
  position:absolute;left:191px;top:23px;width:638px;height:923px;
  transform:scale(1.25);transform-origin:0 0;
  background:var(--paper);overflow:hidden;
  font-family:"Open Sans",sans-serif;color:var(--ink);
}
.hero-photo{
  position:absolute;left:0;top:53px;width:638px;height:784px;
  background:linear-gradient(180deg,#eef0f3 0%,#e3e6ea 55%,#b5563f 72%,#7e2a25 86%,#3b2a4a 100%);
}
.intro-panel{
  position:absolute;left:0;top:53px;width:347px;height:784px;
  background:linear-gradient(180deg,rgba(37,31,108,.97) 0%,rgba(37,31,108,.9) 60%,rgba(32,28,88,.82) 100%);
  color:#fff;font-family:"Montserrat",sans-serif;
}
.quote-mark{position:absolute;left:30px;top:8px;font-size:120px;font-weight:700;line-height:1;font-family:Georgia,serif}
.intro-text{
  position:absolute;left:33px;top:120px;width:300px;
  font-size:28.5px;line-height:37px;font-style:italic;font-weight:400;letter-spacing:.3px;
}
.intro-text strong{font-style:normal;font-weight:700}
.brand{
  position:absolute;left:348px;top:63px;width:257px;height:94px;
  background:rgba(232,233,236,.85);text-align:center;
  font-family:"Montserrat",sans-serif;font-weight:400;color:#3a3848;
}
.brand .name{font-size:22px;letter-spacing:1px;margin-top:12px}
.brand .amp{font-size:18px;line-height:20px}
.brand .sub{font-size:11px;letter-spacing:9px;margin-top:3px;padding-left:8px}
.services-column{position:absolute;left:362px;top:211px;width:243px;height:626px;background:var(--panel-light)}
.banner{
  position:absolute;left:362px;width:243px;background:var(--navy);color:#fff;
  font-family:"Montserrat",sans-serif;font-weight:700;
}
.banner.main{top:170px;height:41px;font-size:27px;line-height:41px;padding-left:26px}
.banner.section{height:26px;font-size:18.5px;line-height:26px;padding-left:24px}
.service{position:absolute;left:362px;width:243px}
.service .tab{position:absolute;left:0;top:18px;width:30px;height:36px;background:var(--navy)}
.service .ring{
  position:absolute;left:21px;top:3px;width:66px;height:66px;border-radius:50%;
  background:#fff;border:5px solid var(--icon-ring);
}
.service .ring .art{position:absolute;left:12px;top:12px;width:32px;height:32px;border-radius:50%;background:radial-gradient(circle,#e3b23a 0 40%,#3e5da8 41% 100%)}
.service p{position:absolute;left:100px;top:8px;width:130px;font-size:10.6px;line-height:13.2px}
.checklist{position:absolute;left:386px;list-style:none;font-size:10.6px;font-weight:600;line-height:19px}
.checklist li{display:flex;align-items:center;gap:5px}
.checklist svg{width:13px;height:11px;flex:none}
.footer{
  position:absolute;left:0;top:848px;width:638px;height:30px;background:var(--footer);
  color:var(--footer-text);font-family:"Montserrat",sans-serif;font-size:16.5px;line-height:30px;
  padding-left:39px;white-space:nowrap;
}
</style>
</head>
<body>
<div class="canvas">
  <article class="flyer">
    <div class="hero-photo" role="img" aria-label="Bright living room with a patterned red rug on the floor"></div>

    <section class="intro-panel">
      <div class="quote-mark">&ldquo;</div>
      <p class="intro-text">The <strong>BRAM</strong><br><strong>Dry Extraction</strong><br>Carpet Cleaning System uses environmentally preferred, Blue Crest Certified cleaning products that deep cleans your carpets and textured hard floors quickly and easily.</p>
    </section>

    <header class="brand">
      <div class="name">VORIK CLEANING</div>
      <div class="amp">&amp;</div>
      <div class="sub">MAINTENANCE</div>
    </header>

    <div class="services-column"></div>
    <h2 class="banner main">Our Services</h2>

    <div class="service" style="top:244px">
      <div class="tab"></div>
      <div class="ring"><div class="art" role="img" aria-label="Cleaning trolley icon"></div></div>
      <p>General Cleaning<br>Carry out heavy cleansing tasks and special projects.</p>
    </div>
    <div class="service" style="top:346px">
      <div class="tab"></div>
      <div class="ring"><div class="art" role="img" aria-label="Floor mop icon"></div></div>
      <p>Clean, stock and supply designated facility areas (dusting, sweeping, vacuuming, mopping, cleaning ceiling vents, restroom cleaning etc).</p>
    </div>
    <div class="service" style="top:453px">
      <div class="tab"></div>
      <div class="ring"><div class="art" role="img" aria-label="Vacuum cleaner icon"></div></div>
      <p>Using electrically pow-ered scrubbing and polishing machines to burnish, scrub, polish and spray clean floors.</p>
    </div>

    <h3 class="banner section" style="top:562px">Window Cleaning</h3>
    <ul class="checklist" style="top:596px">
      <li><svg viewBox="0 0 13 11"><path d="M1 6l3.5 3.5L12 1.5" fill="none" stroke="#2a2274" stroke-width="2.2"/></svg>Regular, Reliable Window Cleaning.</li>
      <li><svg viewBox="0 0 13 11"><path d="M1 6l3.5 3.5L12 1.5" fill="none" stroke="#2a2274" stroke-width="2.2"/></svg>Hard To Reach Windows.</li>
      <li><svg viewBox="0 0 13 11"><path d="M1 6l3.5 3.5L12 1.5" fill="none" stroke="#2a2274" stroke-width="2.2"/></svg>Single 7 Multi-Storey.</li>
      <li><svg viewBox="0 0 13 11"><path d="M1 6l3.5 3.5L12 1.5" fill="none" stroke="#2a2274" stroke-width="2.2"/></svg>Frames and Glass Cleaned.</li>
    </ul>

    <h3 class="banner section" style="top:693px">Floor Cleaning</h3>
    <ul class="checklist" style="top:729px">
      <li><svg viewBox="0 0 13 11"><path d="M1 6l3.5 3.5L12 1.5" fill="none" stroke="#2a2274" stroke-width="2.2"/></svg>Marble Cleaning &amp; Polishing.</li>
      <li><svg viewBox="0 0 13 11"><path d="M1 6l3.5 3.5L12 1.5" fill="none" stroke="#2a2274" stroke-width="2.2"/></svg>Tile &amp; Grout Cleaning.</li>
      <li><svg viewBox="0 0 13 11"><path d="M1 6l3.5 3.5L12 1.5" fill="none" stroke="#2a2274" stroke-width="2.2"/></svg>Hardwood Floors Services.</li>
      <li><svg viewBox="0 0 13 11"><path d="M1 6l3.5 3.5L12 1.5" fill="none" stroke="#2a2274" stroke-width="2.2"/></svg>Vinyl Floors.</li>
    </ul>

    <footer class="footer">010 555 0142 &nbsp;| www.vorikclean.com &nbsp;| hello@vorikclean.com</footer>
  </article>
</div>
</body>
</html>
```